Business Card Design needed for logo design project

This project is linked to Dental Clinic Logo (SEE ATTACHED LOGO FOR GUIDANCE).

Our company needs a Business Card Design. Please refer to our original project in the link above.

Industry/Entity Type

Business

```html
<!DOCTYPE html>
<html lang="en">
<head>
<meta charset="utf-8">
<title>The Glenmore Dental Clinic – Business Card</title>
<link rel="stylesheet" href="https://fonts.googleapis.com/css2?family=Open+Sans:wght@400;600&display=swap">
<style>
  :root {
    --stage-bg: #e9e9e9;
    --stage-glow: #fafafa;
    --card-deep: #1176bb;
    --card-light: #4ba4d5;
    --white: #ffffff;
    --ink-blue: #1a7dc0;
  }
  * { box-sizing: border-box; margin: 0; padding: 0; }
  html, body {
    width: 1200px;
    height: 1000px;
    overflow: hidden;
  }
  body {
    background: radial-gradient(ellipse at center, var(--stage-glow) 0%, var(--stage-bg) 75%);
    font-family: "Open Sans", sans-serif;
    position: relative;
  }
  .business-card {
    position: absolute;
    left: 160px;
    top: 250px;
    width: 880px;
    height: 500px;
    background: linear-gradient(135deg, var(--card-deep) 0%, var(--card-deep) 45%, var(--card-light) 100%);
    box-shadow: 0 18px 40px rgba(0,0,0,0.18);
    color: var(--white);
  }
  .brand {
    position: absolute;
    left: 40px;
    top: 34px;
    display: flex;
    align-items: center;
    gap: 20px;
  }
  .brand-mark {
    width: 60px;
    height: 60px;
    border: 3px solid var(--white);
    border-radius: 8px;
  }
  .brand-name {
    font-weight: 600;
    font-size: 33px;
    line-height: 1.15;
    letter-spacing: 1.5px;
  }
  .name-band {
    position: absolute;
    left: 0;
    right: 0;
    top: 190px;
    height: 90px;
    background: var(--white);
    display: flex;
    align-items: center;
    justify-content: center;
  }
  .band-rule {
    position: absolute;
    left: 0;
    right: 0;
    height: 2px;
    background: var(--white);
  }
  .band-rule.top { top: 182px; }
  .band-rule.bottom { top: 288px; }
  .person-name {
    color: var(--ink-blue);
    font-size: 44px;
    font-weight: 400;
  }
  .person-title {
    position: absolute;
    top: 302px;
    left: 0;
    right: 0;
    text-align: center;
    font-size: 25px;
  }
  .contact-row {
    position: absolute;
    left: 0;
    right: 0;
    display: grid;
    grid-template-columns: repeat(3, 1fr);
    text-align: center;
  }
  .contact-icons { top: 398px; }
  .contact-icons svg { width: 22px; height: 22px; }
  .contact-rule {
    position: absolute;
    left: 0;
    right: 0;
    top: 432px;
    height: 2px;
    background: var(--white);
  }
  .contact-details {
    top: 448px;
    font-size: 26px;
  }
</style>
</head>
<body>
  <section class="business-card">
    <header class="brand">
      <div class="brand-mark"></div>
      <div class="brand-name">The Glenmore<br>Dental Clinic</div>
    </header>

    <div class="band-rule top"></div>
    <div class="name-band"><h1 class="person-name">Declan Moran</h1></div>
    <div class="band-rule bottom"></div>
    <p class="person-title">Principal Dentist/Owner</p>

    <div class="contact-row contact-icons">
      <span><svg viewBox="0 0 24 24" fill="none" stroke="currentColor" stroke-width="1.6"><rect x="6" y="2" width="12" height="20" rx="2"/><line x1="10" y1="18.5" x2="14" y2="18.5"/></svg></span>
      <span><svg viewBox="0 0 24 24" fill="none" stroke="currentColor" stroke-width="1.6"><path d="M3 10 L12 4 L21 10 V20 H3 Z"/><path d="M3 10 L12 16 L21 10"/></svg></span>
      <span><svg viewBox="0 0 24 24" fill="none" stroke="currentColor" stroke-width="1.6"><circle cx="12" cy="12" r="9"/><ellipse cx="12" cy="12" rx="4" ry="9"/><line x1="3" y1="12" x2="21" y2="12"/></svg></span>
    </div>
    <div class="contact-rule"></div>
    <div class="contact-row contact-details">
      <span class="phone">000-000-0000</span>
      <span class="email">name@site.com</span>
      <span class="web">www.website.com</span>
    </div>
  </section>
</body>
</html>
```